TWR Business Card Design

As a full service media and advocacy firm, we lean on years of experience in political and corporate consulting, grassroots campaigning, media placement, and video production to deliver unparalleled results. Recently we have moved into digital media and now provide this service for our clients.

I will add our two company logos to be used on the business cards. The longer logo with "sky reach studio" is our primary logo. Our secondary logo is more square one with "sky reach" and 'digital.media.campaigns" on it. We are looking for clean and modern looking business cards fitting for a digital firm.

I will also add our logos that go well with dark backgrounds.

Industry/Entity Type

Political

Contact Information for Business Card

Walter Pennick, Director of Campaigns and Digital, 555-218-4760, walter@skyreachstudioco.example, @SkyReachStudioCo, @WalterPennick, Facebook.com/SkyReachStudioCo

```html
<!DOCTYPE html>
<html lang="en">
<head>
<meta charset="utf-8">
<title>TWR Business Card</title>
<link rel="stylesheet" href="https://fonts.googleapis.com/css2?family=Open+Sans:wght@400;600;700&display=swap">
<style>
  :root {
    --backdrop: #111111;
    --blue-light: #3a8bca;
    --blue-deep: #243c7e;
    --blue-text: #3a86c8;
    --ink: #2b2b2b;
    --paper: #ffffff;
    --rule: #b9b9b9;
    --icon-navy: #23346f;
  }
  * { margin: 0; padding: 0; box-sizing: border-box; }
  html, body { width: 1200px; height: 1000px; overflow: hidden; background: var(--backdrop); }
  body { position: relative; font-family: "Open Sans", Arial, sans-serif; }

  .card {
    position: absolute;
    left: 260px;
    width: 680px;
    border-radius: 24px;
    box-shadow: 0 6px 18px rgba(0,0,0,0.55);
    overflow: hidden;
  }
  .card--front {
    top: 90px;
    height: 385px;
    background: linear-gradient(180deg, var(--blue-light) 0%, #3677b8 40%, var(--blue-deep) 85%);
  }
  .card--back {
    top: 521px;
    height: 387px;
    background: var(--paper);
  }

  .wordmark {
    position: absolute;
    display: flex;
    align-items: center;
    gap: 16px;
    font-weight: 600;
    letter-spacing: 1px;
    white-space: nowrap;
  }
  .wordmark__dot { border-radius: 50%; flex: none; }

  .card--front .wordmark {
    left: 0; right: 0; top: 130px;
    justify-content: center;
    color: var(--paper);
    font-size: 76px;
    line-height: 1;
  }
  .card--front .wordmark__dot { width: 26px; height: 26px; background: var(--paper); }

  .card--back .wordmark {
    left: 34px; width: 300px; top: 158px;
    justify-content: center;
    color: var(--blue-text);
    font-size: 44px;
    line-height: 1;
  }
  .card--back .wordmark__dot { width: 16px; height: 16px; background: var(--blue-text); }

  .divider {
    position: absolute;
    left: 342px; top: 58px;
    width: 2px; height: 302px;
    background: linear-gradient(180deg, rgba(185,185,185,0) 0%, var(--rule) 30%, var(--rule) 70%, rgba(185,185,185,0) 100%);
  }

  .contact-block { position: absolute; left: 376px; top: 110px; color: var(--ink); }
  .contact-block__name { font-size: 26px; font-weight: 700; line-height: 1.1; letter-spacing: -0.2px; }
  .contact-block__title { font-size: 16px; color: var(--blue-text); margin-top: 4px; }
  .contact-list { list-style: none; margin-top: 16px; }
  .contact-list li {
    display: flex; align-items: center; gap: 6px;
    font-size: 16.5px; line-height: 22.5px;
  }
  .contact-list svg { width: 16px; height: 16px; flex: none; }
  .contact-list .icon-square { width: 14px; height: 14px; background: var(--icon-navy); border-radius: 2px; margin: 0 1px; flex: none; }
</style>
</head>
<body>
  <section class="card card--front" aria-label="Card front">
    <div class="wordmark"><span class="wordmark__dot"></span>SKY REACH</div>
  </section>

  <section class="card card--back" aria-label="Card back">
    <div class="wordmark"><span class="wordmark__dot"></span>SKY REACH</div>
    <div class="divider"></div>
    <div class="contact-block">
      <h1 class="contact-block__name">Walter Pennick</h1>
      <p class="contact-block__title">Director of Campaigns and Digital</p>
      <ul class="contact-list">
        <li>
          <svg viewBox="0 0 16 16" aria-hidden="true"><path fill="#23346f" d="M1 6c0-2 3-4 7-4s7 2 7 4l-3 1-1-2H5L4 7 1 6zm3 2h8l2 6H2l2-6zm4 1.5a2 2 0 1 0 0 4 2 2 0 0 0 0-4z"/></svg>
          555-218-4760
        </li>
        <li>
          <svg viewBox="0 0 16 16" aria-hidden="true"><rect x="1" y="3" width="14" height="10" fill="#23346f"/><path d="M1.5 3.5 8 9l6.5-5.5M1.5 12.5 6 8m8.5 4.5L10 8" stroke="#fff" stroke-width="1.2" fill="none"/></svg>
          walter@skyreachstudioco.example
        </li>
        <li><span class="icon-square"></span>@SkyReachStudioCo</li>
        <li><span class="icon-square"></span>/SkyReachStudioCo</li>
        <li><span class="icon-square"></span>@WalterPennick</li>
      </ul>
    </div>
  </section>
</body>
</html>
```